Editorial Website Design for High-End Custom Millwork Firm

Design (no development) for a 5-7 page website for a high-end custom architectural millwork firm. Editorial, magazine-quality aesthetic — think Dwelling Quarterly and top-tier millwork studios (Owen Tallard, Vorko). Full brief, reference sites, and project photography attached. We have uploaded a sample of our photography to use in your design. PLEASE READ PDF DOCUMENT BRIEF!!!

```html
<!DOCTYPE html>
<html lang="en">
<head>
<meta charset="utf-8">
<title>Alder Millwork — Website Design</title>
<link href="https://fonts.googleapis.com/css2?family=Cormorant+Garamond:wght@300;400&family=Inter:wght@400;500&display=swap" rel="stylesheet">
<style>
:root{
  --charcoal:#393B3C;
  --walnut:#5D4037;
  --sand:#EAD8B8;
  --linen:#F8F2E6;
  --paper:#F9F9F9;
  --board:#E4E4E4;
  --panel:#F2EEE6;
  --rule:#BDBAB4;
  --muted:#8E8B86;
  --serif:"Cormorant Garamond",Georgia,serif;
  --sans:"Inter",Helvetica,Arial,sans-serif;
}
*{margin:0;padding:0;box-sizing:border-box}
html,body{width:1200px;height:3343px;overflow:hidden}
body{background:var(--board);position:relative;font-family:var(--sans);color:var(--charcoal)}
.abs{position:absolute}
.serif{font-family:var(--serif);font-weight:300}
.sans{font-family:var(--sans)}
.label{font-family:var(--sans);font-size:6px;letter-spacing:.06em;text-transform:uppercase;color:var(--muted);line-height:1}
.link{font-family:var(--sans);font-size:7px;letter-spacing:.03em;text-transform:uppercase;line-height:1;padding-bottom:4px;border-bottom:1px solid var(--charcoal)}
.photo{position:absolute}
.rule{position:absolute;height:1px;background:var(--rule)}
.wordmark-band{left:50%;transform:translateX(-50%);white-space:nowrap;color:#fff;font-family:var(--serif);font-weight:300}

/* style guide */
.brand-mark{left:309px;top:82px;width:83px;height:44px;font-family:var(--serif);font-size:36px;font-weight:300;color:var(--charcoal);text-align:center;line-height:44px}
.guide-title{font-family:var(--sans);font-size:20px;line-height:1}
.swatch{position:absolute;width:34px;height:34px;border-radius:50%;top:109px}
.hex{position:absolute;top:150px;font-size:6.5px;width:44px;text-align:center;font-family:var(--sans)}

/* desktop page */
.desk{left:185px;top:211px;width:584px;height:3042px;background:var(--paper);overflow:hidden}
.site-header{left:0;top:0;width:584px;height:33px;background:#fff;border-bottom:1px solid var(--rule)}
.menu-box{background:var(--walnut)}
.burger span{display:block;height:1.5px;background:#fff;margin:3px 0}
.list{font-family:var(--sans);font-size:10px;line-height:23px}
.card-title{font-family:var(--sans);font-size:15px;line-height:1}
.site-footer{background:var(--charcoal);color:#fff}
.f-label{font-family:var(--sans);font-size:6px;color:#9c9c9c;line-height:1}
.f-val{font-family:var(--sans);font-size:11px;font-weight:500;color:#fff;line-height:1.3}
.nav-item{font-size:6.5px;color:#fff;font-weight:500;line-height:1}

/* mobile page */
.phone{left:916px;top:214px;width:173px;height:2403px;background:var(--paper);overflow:hidden}
.m-list{font-family:var(--sans);font-size:9.5px;line-height:24.7px;white-space:nowrap}
.m-val{font-family:var(--sans);font-size:9px;font-weight:500;color:#fff;line-height:1.4}
</style>
</head>
<body>

<!-- Style guide -->
<div class="abs brand-mark">AMW</div>

<div class="abs guide-title" style="left:508px;top:81px">Fonts:</div>
<div class="abs sans" style="left:510px;top:115px;font-size:15px">Halden Sans</div>
<div class="abs serif" style="left:510px;top:131px;font-size:16px;font-weight:400">Morrow Serif</div>

<div class="abs guide-title" style="left:694px;top:81px">Colors:</div>
<div class="swatch" style="left:694px;background:var(--charcoal)"></div>
<div class="swatch" style="left:733px;background:var(--walnut)"></div>
<div class="swatch" style="left:774px;background:var(--sand)"></div>
<div class="swatch" style="left:816px;background:var(--linen)"></div>
<div class="swatch" style="left:857px;background:#fff;border:1px solid #ddd"></div>
<div class="hex" style="left:689px">#393B3C</div>
<div class="hex" style="left:728px">#5D4037</div>
<div class="hex" style="left:769px">#EAD8B8</div>
<div class="hex" style="left:811px">#F8F2E6</div>
<div class="hex" style="left:852px">#F9F9F9</div>

<!-- Desktop page -->
<main class="abs desk">
  <header class="abs site-header">
    <div class="abs serif" style="left:12px;top:6px;font-size:20px;font-weight:400">AMW</div>
    <div class="abs menu-box burger" style="left:519px;top:0;width:31px;height:33px;padding:10px 8px">
      <span></span><span style="margin-left:4px"></span><span></span>
    </div>
    <svg class="abs" style="left:561px;top:11px" width="12" height="12" viewBox="0 0 12 12" fill="none" stroke="#393B3C" stroke-width="1.1"><circle cx="5" cy="5" r="3.8"/><line x1="7.8" y1="7.8" x2="11" y2="11"/></svg>
  </header>

  <h1 class="abs serif" style="left:0;top:66px;width:584px;text-align:center;font-size:35px;line-height:36px">Timeless custom millwork &amp;<br>architectural woodwork</h1>
  <div class="abs" style="left:0;top:159px;width:584px;text-align:center"><span class="link" style="font-size:6.5px">Our Capabilities</span></div>

  <div class="abs" role="img" aria-label="Bright kitchen with cream cabinetry, brass pendants and a white-oak island" style="left:10px;top:204px;width:566px;height:324px;overflow:hidden;background:linear-gradient(180deg,#ECE6DA 0%,#E3DACB 45%,#B8936B 72%,#D9CFBF 100%)">
    <div class="abs wordmark-band" style="top:248px;font-size:88px;line-height:84px">ALDER MILLWORK</div>
  </div>

  <p class="abs serif" style="left:94px;top:584px;width:396px;text-align:center;font-size:18.5px;line-height:26px">We put the full power of our knowledge, facilities, and craftsmanship to work for you in the most <span style="font-weight:400">cost-effective</span> way possible.</p>

  <div class="abs label" style="left:25px;top:709px">What we do</div>
  <div class="rule" style="left:25px;top:722px;width:534px"></div>

  <!-- Residential -->
  <div class="abs" style="left:120px;top:725px;width:464px;height:279px;background:var(--panel)"></div>
  <div class="abs" style="left:25px;top:749px;width:95px;height:229px;background:var(--panel)"></div>
  <div class="photo" role="img" aria-label="Kitchen with white-oak cabinetry and marble backsplash" style="left:25px;top:749px;width:271px;height:229px;background:linear-gradient(120deg,#E9E5DE 0%,#D8CFC2 45%,#C49A6C 100%)"></div>
  <h2 class="abs serif" style="left:327px;top:770px;font-size:25px;line-height:30px">Residential Millwork</h2>
  <div class="abs list" style="left:327px;top:816px">Built-In Cabinetry<br>Custom Closets &amp; Storage<br>Kitchen, Room and Bath Cabinetry<br>Libraries and Improvised Home Offices<br>Wall Paneling and Trim</div>
  <div class="abs link" style="left:461px;top:947px;font-size:6.5px">Explore Details</div>

  <!-- Commercial -->
  <div class="abs" style="left:452px;top:1004px;width:132px;height:127px;background:var(--panel)"></div>
  <h2 class="abs serif" style="left:25px;top:1050px;font-size:25px;line-height:30px">Commercial Millwork</h2>
  <div class="abs list" style="left:25px;top:1093px">Architectural Woodwork<br>Custom Cabinetry<br>Interior Wood Finishes<br>Reception and Feature Walls<br>Store Fixtures and Casework</div>
  <div class="abs link" style="left:25px;top:1224px;font-size:6.5px">Explore Details</div>
  <div class="photo" role="img" aria-label="Hotel reception with walnut desks, a screened feature wall and a living green wall" style="left:288px;top:1028px;width:268px;height:228px;background:linear-gradient(180deg,#8C8680 0%,#6E4A35 45%,#A98A75 75%,#5E6B55 100%)"></div>

  <!-- Process card -->
  <section class="abs" style="left:13px;top:1310px;width:558px;height:445px;border:1px solid var(--rule);background:#fff">
    <p class="abs serif" style="left:60px;top:46px;width:438px;text-align:center;font-size:19.5px;line-height:25px">From the workshop to the final installation, every project is guided by skilled craftsmen, proven processes, and decades of experience.</p>
    <div class="abs" style="left:0;top:143px;width:556px;text-align:center"><span class="link" style="font-size:6.5px">Discover the Process</span></div>
    <div class="photo" role="img" aria-label="Finisher spraying walnut mouldings in the finishing booth" style="left:0;top:193px;width:279px;height:179px;background:linear-gradient(110deg,#C9C6C2 0%,#A9A6A2 55%,#6F4E3C 100%)"></div>
    <div class="photo" role="img" aria-label="Craftsman assembling a curved oak frame in the workshop" style="left:279px;top:193px;width:277px;height:179px;background:linear-gradient(110deg,#3F3C3A 0%,#6A625A 45%,#C9A57E 100%)"></div>
    <div class="abs" style="left:0;top:372px;width:556px;height:71px;background:var(--linen)"></div>
    <div class="abs" style="left:215px;top:392px;width:40px;height:40px;border-radius:50%;background:var(--charcoal)"></div>
    <div class="abs" style="left:278px;top:396px;width:32px;height:32px;background:var(--charcoal)"></div>
  </section>

  <!-- Resources -->
  <div class="abs label" style="left:25px;top:1809px">Resources and insights</div>
  <div class="rule" style="left:25px;top:1822px;width:534px"></div>
  <h2 class="abs serif" style="left:25px;top:1832px;width:290px;font-size:21px;line-height:25px">Explore exceptional projects that bring great architecture to life</h2>
  <div class="abs link" style="right:24px;top:1909px;font-size:6.5px">Browse all stories</div>

  <div class="photo" role="img" aria-label="Open co-working loft with round white tables" style="left:25px;top:1907px;width:254px;height:153px;background:linear-gradient(180deg,#D9D7D2 0%,#B4ADA3 55%,#8E7458 100%)"></div>
  <div class="abs label" style="left:25px;top:2075px;font-size:5px">New York City</div>
  <div class="abs card-title" style="left:25px;top:2087px">Tallow Loft</div>
  <div class="rule" style="left:25px;top:2116px;width:254px"></div>

  <div class="photo" role="img" aria-label="Fluted white-oak kitchen island end" style="left:25px;top:2141px;width:254px;height:293px;background:linear-gradient(90deg,#EDEAE6 0%,#D6BE9E 45%,#C6A47D 100%)"></div>
  <div class="abs label" style="left:25px;top:2446px;font-size:5px">New York City</div>
  <div class="abs card-title" style="left:25px;top:2459px">Brennick Kitchen</div>
  <div class="rule" style="left:25px;top:2489px;width:254px"></div>

  <div class="photo" role="img" aria-label="Open co-working loft with round white tables" style="left:25px;top:2513px;width:254px;height:153px;background:linear-gradient(180deg,#D9D7D2 0%,#B4ADA3 55%,#8E7458 100%)"></div>
  <div class="abs label" style="left:25px;top:2680px;font-size:5px">New York City</div>
  <div class="abs card-title" style="left:25px;top:2692px">Tallow Loft</div>
  <div class="rule" style="left:25px;top:2722px;width:254px"></div>

  <div class="photo" role="img" aria-label="Oak reception desk below framed artwork" style="left:304px;top:1954px;width:256px;height:294px;background:linear-gradient(180deg,#F1EFEB 0%,#E2D8CA 50%,#A98A68 80%,#D8CDBE 100%)"></div>
  <div class="abs label" style="left:304px;top:2261px;font-size:5px">New York City</div>
  <div class="abs card-title" style="left:304px;top:2272px">Brennick Kitchen</div>
  <div class="rule" style="left:304px;top:2303px;width:256px"></div>

  <div class="photo" role="img" aria-label="Open co-working loft with round white tables" style="left:304px;top:2327px;width:256px;height:153px;background:linear-gradient(180deg,#D9D7D2 0%,#B4ADA3 55%,#8E7458 100%)"></div>
  <div class="abs label" style="left:304px;top:2494px;font-size:5px">New York City</div>
  <div class="abs card-title" style="left:304px;top:2506px">Tallow Loft</div>
  <div class="rule" style="left:304px;top:2535px;width:256px"></div>

  <!-- Footer -->
  <footer class="abs site-footer" style="left:0;top:2775px;width:584px;height:267px">
    <div class="abs f-label" style="left:25px;top:42px">Phone</div>
    <div class="abs f-val" style="left:25px;top:53px">919.555.0142</div>
    <div class="abs f-label" style="left:25px;top:85px">General Inquiries</div>
    <div class="abs f-val" style="left:25px;top:96px">info@aldermillwork.com</div>
    <div class="abs f-label" style="left:25px;top:126px">Address</div>
    <div class="abs f-val" style="left:25px;top:138px">1140 Linden Row<br>Durham, NC 27701</div>
    <div class="abs f-label" style="left:183px;top:42px">Architects and Interior Design</div>
    <div class="abs f-val" style="left:183px;top:53px">hollis@aldermillwork.com</div>
    <div class="abs f-label" style="left:183px;top:85px">General Contractor and Construction Manager</div>
    <div class="abs f-val" style="left:183px;top:96px">dean@aldermillwork.com</div>
    <div class="abs link" style="left:457px;top:43px;color:#fff;border-color:#fff;font-size:6.5px">Schedule a Project</div>
    <div class="rule" style="left:25px;top:210px;width:534px;background:#4a4c4d"></div>
    <nav>
      <div class="abs nav-item" style="left:38px;top:221px">Portfolio</div>
      <div class="abs nav-item" style="left:86px;top:221px">Capabilities</div>
      <div class="abs nav-item" style="left:143px;top:221px">Story</div>
      <div class="abs nav-item" style="left:183px;top:221px">Process</div>
      <div class="abs nav-item" style="left:230px;top:221px">Resources</div>
      <div class="abs nav-item" style="left:284px;top:221px">Contact</div>
    </nav>
    <div class="abs f-label" style="left:457px;top:221px">2026 · Alder Architectural Millwork</div>
    <div class="abs f-label" style="right:24px;top:251px;color:#fff">BACK TO TOP</div>
  </footer>
</main>

<!-- Mobile page -->
<main class="abs phone">
  <header class="abs" style="left:0;top:13px;width:173px;height:28px;background:#fff">
    <svg class="abs" style="left:8px;top:9px" width="11" height="11" viewBox="0 0 12 12" fill="none" stroke="#393B3C" stroke-width="1.1"><circle cx="5" cy="5" r="3.8"/><line x1="7.8" y1="7.8" x2="11" y2="11"/></svg>
    <div class="abs serif" style="left:0;top:5px;width:173px;text-align:center;font-size:16px;font-weight:400">AMW</div>
    <div class="abs menu-box burger" style="left:145px;top:0;width:26px;height:28px;padding:8px 6px"><span></span><span style="margin-left:3px"></span><span></span></div>
  </header>
  <div class="abs" style="left:0;top:52px;width:173px;height:172px;background:#F1F0EE"></div>
  <h1 class="abs serif" style="left:0;top:65px;width:173px;text-align:center;font-size:20px;line-height:25px">Timeless custom<br>millwork and<br>architectural<br>woodwork</h1>
  <div class="abs" style="left:0;top:185px;width:173px;text-align:center"><span class="link" style="font-size:6.5px">Our Capabilities</span></div>
  <div class="abs" role="img" aria-label="Bright kitchen with cream cabinetry and a white-oak island" style="left:0;top:224px;width:173px;height:146px;overflow:hidden;background:linear-gradient(180deg,#ECE6DA 0%,#E3DACB 45%,#B8936B 75%,#D9CFBF 100%)">
    <div class="abs wordmark-band" style="top:118px;font-size:30px;line-height:30px">ALDER MILLWORK</div>
  </div>

  <p class="abs serif" style="left:10px;top:398px;width:153px;text-align:center;font-size:14.5px;line-height:18px">We put the full power of our knowledge, facilities, and craftsmanship to work for you in the most cost-effective way possible.</p>

  <div class="abs label" style="left:9px;top:547px;font-size:5px">What we do</div>
  <div class="rule" style="left:9px;top:562px;width:155px"></div>
  <div class="abs" style="left:152px;top:590px;width:21px;height:280px;background:var(--panel)"></div>
  <div class="photo" role="img" aria-label="Kitchen with white-oak cabinetry and marble backsplash" style="left:10px;top:589px;width:155px;height:124px;background:linear-gradient(120deg,#E9E5DE 0%,#D8CFC2 45%,#C49A6C 100%)"></div>
  <h2 class="abs serif" style="left:9px;top:735px;font-size:18.5px;line-height:22px;white-space:nowrap">Residential Millwork</h2>
  <div class="abs m-list" style="left:9px;top:767px">Built-In Cabinetry<br>Custom Closets &amp; Storage<br>Kitchen and Bath Cabinetry<br>Libraries and Home Offices<br>Wall Paneling and Trim</div>
  <div class="abs link" style="left:9px;top:906px;font-size:6.5px">Explore Details</div>

  <div class="photo" role="img" aria-label="Hotel reception with walnut desks and a screened feature wall" style="left:10px;top:970px;width:155px;height:125px;background:linear-gradient(180deg,#8C8680 0%,#6E4A35 45%,#A98A75 75%,#5E6B55 100%)"></div>
  <h2 class="abs serif" style="left:9px;top:1116px;font-size:18.5px;line-height:22px;white-space:nowrap">Commercial Millwork</h2>
  <div class="abs m-list" style="left:9px;top:1149px">Architectural Woodwork<br>Custom Cabinetry<br>Interior Wood Finishes<br>Reception and Feature Walls<br>Store Fixtures and Casework</div>
  <div class="abs link" style="left:9px;top:1287px;font-size:6.5px">Explore Details</div>

  <section class="abs" style="left:4px;top:1351px;width:166px;height:316px;border:1px solid var(--rule);background:#fff">
    <p class="abs serif" style="left:10px;top:33px;width:144px;text-align:center;font-size:14.5px;line-height:18px">From the workshop to the final installation, every project is guided by skilled craftsmen, proven processes, and decades of experience.</p>
    <div class="abs" style="left:0;top:161px;width:164px;text-align:center"><span class="link" style="font-size:6.5px">Discover the Process</span></div>
    <div class="photo" role="img" aria-label="Finisher spraying walnut mouldings" style="left:0;top:204px;width:82px;height:55px;background:linear-gradient(110deg,#C9C6C2 0%,#A9A6A2 55%,#6F4E3C 100%)"></div>
    <div class="photo" role="img" aria-label="Craftsman assembling a curved oak frame" style="left:82px;top:204px;width:82px;height:55px;background:linear-gradient(110deg,#3F3C3A 0%,#6A625A 45%,#C9A57E 100%)"></div>
    <div class="abs" style="left:0;top:259px;width:164px;height:55px;background:var(--linen)"></div>
    <div class="abs" style="left:34px;top:273px;width:28px;height:28px;border-radius:50%;background:var(--charcoal)"></div>
    <div class="abs" style="left:80px;top:276px;width:22px;height:22px;background:var(--charcoal)"></div>
  </section>

  <div class="abs label" style="left:9px;top:1709px;font-size:5px">Resources and insights</div>
  <div class="rule" style="left:9px;top:1721px;width:155px"></div>
  <h2 class="abs serif" style="left:9px;top:1745px;width:150px;font-size:15.5px;line-height:18px">Explore exceptional projects that bring great architecture to life</h2>
  <div class="photo" role="img" aria-label="Open co-working loft with round white tables" style="left:2px;top:1818px;width:161px;height:121px;background:linear-gradient(180deg,#D9D7D2 0%,#B4ADA3 55%,#8E7458 100%)"></div>
  <div class="photo" role="img" aria-label="Next project image" style="left:168px;top:1818px;width:10px;height:121px;background:#B4ADA3"></div>
  <div class="abs label" style="left:9px;top:1955px;font-size:4.5px">New York City</div>
  <div class="abs card-title" style="left:9px;top:1966px;font-size:14px">Tallow Loft</div>
  <div class="rule" style="left:9px;top:1997px;width:155px"></div>
  <div class="abs link" style="left:9px;top:2020px;font-size:6.5px">Browse all resources</div>

  <footer class="abs site-footer" style="left:0;top:2071px;width:173px;height:332px">
    <div class="abs f-label" style="left:9px;top:41px">Phone</div>
    <div class="abs m-val" style="left:9px;top:53px">919.555.0142</div>
    <div class="abs f-label" style="left:9px;top:80px">General Inquiries</div>
    <div class="abs m-val" style="left:9px;top:93px">info@aldermillwork.com</div>
    <div class="abs f-label" style="left:9px;top:120px">Address</div>
    <div class="abs m-val" style="left:9px;top:132px">1140 Linden Row<br>Durham, NC 27701</div>
    <div class="abs f-label" style="left:9px;top:172px">Architects and Interior Design</div>
    <div class="abs m-val" style="left:9px;top:185px">hollis@aldermillwork.com</div>
    <div class="abs f-label" style="left:9px;top:213px">General Contractor and Construction Manager</div>
    <div class="abs m-val" style="left:9px;top:225px">dean@aldermillwork.com</div>
    <div class="rule" style="left:9px;top:270px;width:155px;background:#4a4c4d"></div>
    <div class="abs f-label" style="left:0;top:287px;width:173px;text-align:center;font-size:5px">2026 · Alder Architectural Millwork</div>
    <div class="abs f-label" style="right:9px;top:314px;color:#fff;font-size:5px">BACK TO TOP</div>
  </footer>
</main>

</body>
</html>
```